Create a Graphic About YOURSELF and PixelHarbor

PixelHarbor would like you (designers) to create an awesome graphic to promote YOURSELF and your profile on PixelHarbor!

Your graphic should communicate your name, your services and should mention PixelHarbor.

The design should be perfect for sharing on Chatterly. Here's an example of what we'd like http://blog.pixelharbor-example.ca/article/333/pixelharbor-launches-3000-hire-me-social-design-contest

Once you submitted your design, we'd love you to share the design ('advertisement') and promote yourself and PixelHarbor to your friends and potential customers. So make your submissions great and get your friends to vote for your design by 'Liking' it on Chatterly!

Prizes:
$1500 - "PixelHarbor Community" prize awarded to the designer with the most Chatterly 'Likes'
5 x $50 for the next 5 'most liked' designs on Chatterly

$1000 - "Hire Me" prize awarded to the designer who receives the most client invites
5 x $50 for the next 5 'most invited' designers

In summary, this is a great opportunity for you to increase your exposure to PixelHarbor customers and win cash prizes. Show off your design skills and get hired by PixelHarbor customers from around the world!

Target Market(s)

Fans, friends and customers of YOU

Industry/Entity Type

Cash

Requirements
Must have
• 1) Include your PixelHarbor user name on the graphic so customers can find you in the PixelHarbor Designer Directory
2) Include the tagline "Hire Me on PixelHarbor.com!" in your graphic design.
3) Share your design's URL on our Chatterly wall at http://chatterly-example.com/pixelharbor and get your friends to 'like' your design.
Nice to have
• 1) Include a tagline that expresses your design approach/philosophy
2) Artwork dimensions: 403 x 403 px
3) You can submit more than 1 design!
Should not have
• You must own the copyright of any images you use including stock imagery.

```html
<!DOCTYPE html>
<html lang="en">
<head>
<meta charset="utf-8">
<title>Hey, You! — Hire Me on PixelHarbor</title>
<link rel="stylesheet" href="https://fonts.googleapis.com/css2?family=Bebas+Neue&display=swap">
<style>
  :root {
    --bg-orange: #f7941d;
    --text-white: #ffffff;
    --accent-yellow: #fff200;
    --accent-red: #ef5a29;
  }
  html, body {
    margin: 0;
    padding: 0;
    width: 1200px;
    height: 1200px;
    overflow: hidden;
  }
  .promo-card {
    position: relative;
    width: 1200px;
    height: 1200px;
    background: var(--bg-orange);
    font-family: "Bebas Neue", "Oswald", sans-serif;
    line-height: 1;
    overflow: hidden;
  }
  .promo-card > * {
    position: absolute;
    margin: 0;
    font-weight: 400;
    white-space: nowrap;
  }
  .headline {
    top: 98px;
    left: 0;
    width: 1200px;
    text-align: center;
    font-size: 362px;
    color: var(--text-white);
    letter-spacing: 2px;
  }
  .subheadline {
    top: 522px;
    left: 0;
    width: 1200px;
    text-align: center;
    font-size: 136px;
    color: var(--text-white);
  }
  .hire-tagline {
    top: 776px;
    left: 381px;
    font-size: 43px;
    color: var(--accent-yellow);
  }
  .designer-name {
    top: 855px;
    left: 381px;
    font-size: 93px;
    color: var(--accent-red);
  }
  .services {
    top: 951px;
    left: 381px;
    font-size: 77px;
    line-height: 0.77;
    color: var(--accent-red);
  }
  .philosophy {
    top: 1113px;
    left: 381px;
    font-size: 43px;
    color: var(--text-white);
  }
</style>
</head>
<body>
  <main class="promo-card">
    <h1 class="headline">Hey, You!</h1>
    <p class="subheadline">Yeah, You!</p>
    <p class="hire-tagline">Hire Me on PixelHarbor.com</p>
    <h2 class="designer-name">Mara Delvecchio</h2>
    <p class="services">Corporate Identity<br>Promotional Design</p>
    <p class="philosophy">Design That Demands Attention</p>
  </main>
</body>
</html>
```